The Calder & Wimms Irish Bar Bendigo

I need an app for my local hotel/pub. We have a bistro, functions and live entertainment every week. I would like to promote meal deals, drink offers, upcoming shows, members benefits. I would need to be able to update daily. Thanks
Updates

Reason: I am away on holidays until 19th July and can only get contact rarely so follow up is only on my phone not computer. Thanks Gareth

Target Market(s)

18+

Industry/Entity Type

Entertainment

Requirements
Must have
• Promotions
Entertainment
Functions
About the hotel

```html
<!DOCTYPE html>
<html lang="en">
<head>
<meta charset="utf-8">
<title>The Calder &amp; Wimms Irish Bar – App Screens</title>
<link rel="stylesheet" href="https://fonts.googleapis.com/css2?family=Dosis:wght@500;600&family=Lato:wght@400&display=swap">
<style>
  :root {
    --stage-light: #ffffff;
    --stage-dark: #b9b9b9;
    --header-top: #5a5a5a;
    --header-mid: #1b1b1b;
    --header-bottom: #000000;
    --header-rim: #cfd3d6;
    --content-top: #dff6f6;
    --content-bottom: #aadddd;
    --card: #f1f1f1;
    --card-text: #5b5b5b;
    --date-red: #c8102e;
    --sticker-light: #ffc84a;
    --sticker-dark: #f49a10;
    --nav-top: #6d6d72;
    --nav-bottom: #1d1d22;
    --nav-base: #0a0a0c;
    --icon: #ffffff;
    --icon-active: #f5e21a;
    --dot: #f7a457;
    --social: #6d8fa8;
    --caption: #8a8a8a;
  }
  * { box-sizing: border-box; margin: 0; padding: 0; }
  html, body { width: 1200px; height: 661px; overflow: hidden; }
  body {
    position: relative;
    background: radial-gradient(ellipse at 50% 35%, var(--stage-light) 0%, #e9e9e9 45%, var(--stage-dark) 100%);
    font-family: "Lato", sans-serif;
  }
  .screen {
    position: absolute; top: 89px; width: 310px; height: 461px; overflow: hidden;
    background: linear-gradient(180deg, var(--content-top) 0%, var(--content-bottom) 100%);
    box-shadow: 6px 8px 10px rgba(0,0,0,.35);
  }
  .screen--drinks { left: 66px; }
  .screen--shows { left: 418px; }
  .screen--meals { left: 784px; }
  .screen__header {
    position: absolute; top: 0; left: 0; width: 100%; height: 44px; z-index: 5;
    background: linear-gradient(180deg, var(--header-rim) 0%, var(--header-top) 12%, var(--header-mid) 70%, var(--header-bottom) 100%);
    color: #fff; text-align: center; text-transform: uppercase;
    font-family: "Dosis", sans-serif; font-weight: 600; font-size: 18px; letter-spacing: .5px; line-height: 42px;
  }
  .screen__header::after {
    content: ""; position: absolute; left: 50%; bottom: -7px; margin-left: -7px;
    border-left: 7px solid transparent; border-right: 7px solid transparent; border-top: 7px solid #000;
  }
  .photo { position: absolute; border: 2px solid #fff; box-shadow: 1px 2px 4px rgba(0,0,0,.3); }
  .sticker {
    position: absolute; border-radius: 50%;
    background: radial-gradient(circle at 35% 30%, var(--sticker-light) 0%, var(--sticker-dark) 100%);
    border: 2px solid #fff; box-shadow: 2px 3px 5px rgba(0,0,0,.35);
    color: #fff; font-family: "Dosis", sans-serif; font-weight: 600; text-align: center;
    display: flex; align-items: center; justify-content: center;
  }
  .card {
    position: absolute; background: var(--card); color: var(--card-text);
    box-shadow: 1px 2px 4px rgba(0,0,0,.25); padding: 8px 9px;
  }
  .card__date {
    font-family: "Dosis", sans-serif; font-weight: 600; color: var(--date-red);
    text-transform: uppercase; font-size: 14px; line-height: 18px;
  }
  .card__act { font-size: 14px; line-height: 17px; }
  .card__act--small { font-size: 12.5px; line-height: 15px; }
  .description { position: absolute; left: 133px; top: 179px; width: 171px; height: 161px; }
  .description .card__date { font-size: 14px; margin-bottom: 3px; }
  .description p { font-size: 8.5px; line-height: 11.5px; }
  .social { position: absolute; left: 94px; top: 351px; display: flex; gap: 3px; }
  .social span { width: 26px; height: 26px; border-radius: 3px; background: var(--social); }
  .nav { position: absolute; left: 0; bottom: 0; width: 310px; height: 110px; z-index: 4; }
  .caption {
    position: absolute; left: 66px; top: 575px; color: var(--caption);
    font-family: "Dosis", sans-serif; font-weight: 500; font-size: 10.5px; text-transform: uppercase; letter-spacing: .2px;
  }
</style>
</head>
<body>

<svg width="0" height="0" style="position:absolute" aria-hidden="true">
  <defs>
    <linearGradient id="navFill" x1="0" y1="0" x2="0" y2="1">
      <stop offset="0" stop-color="var(--nav-top)"/>
      <stop offset=".6" stop-color="var(--nav-bottom)"/>
      <stop offset="1" stop-color="var(--nav-base)"/>
    </linearGradient>
    <g id="navBase">
      <path d="M0 8 Q155 70 310 8 L310 110 L0 110 Z" fill="#e8fbfb"/>
      <path d="M0 14 Q155 78 310 14 L310 110 L0 110 Z" fill="url(#navFill)"/>
      <rect x="0" y="100" width="310" height="10" fill="var(--nav-base)"/>
      <circle cx="66" cy="70" r="4" fill="var(--dot)"/>
      <circle cx="139" cy="70" r="4" fill="var(--dot)"/>
      <circle cx="224" cy="70" r="4" fill="var(--dot)"/>
    </g>
    <g id="iconMeal">
      <path d="M-7 -14 v9 a3 3 0 0 0 6 0 v-9 M-4 -14 v28" fill="none" stroke-width="2.2"/>
      <path d="M5 14 v-28 c4 3 4 12 0 15" fill="none" stroke-width="2.6"/>
    </g>
    <g id="iconDrink">
      <path d="M-9 -8 h16 l-2 22 h-12 Z" fill="none" stroke-width="2"/>
      <path d="M-6 2 h10 l-1 10 h-8 Z" stroke="none"/>
      <path d="M2 -8 l5 -9" fill="none" stroke-width="1.6"/>
      <circle cx="-7" cy="-11" r="4" stroke="none"/>
    </g>
    <g id="iconShow">
      <path d="M-12 -14 h9 l2 28 h-13 Z M3 -14 h9 l2 28 h-13 Z" stroke="none"/>
    </g>
    <g id="iconMembers" fill="none" stroke-width="2">
      <circle cx="-4" cy="-5" r="5"/><path d="M-13 10 a9 7 0 0 1 18 0 Z"/>
      <circle cx="6" cy="-8" r="5"/><path d="M3 6 h12 a9 7 0 0 0 -12 -8"/>
    </g>
  </defs>
</svg>

<!-- Drinks offers -->
<section class="screen screen--drinks">
  <header class="screen__header">Drinks Offers</header>
  <div class="photo" style="left:20px;top:61px;width:164px;height:221px;background:linear-gradient(135deg,#c9d3d6 0%,#8d979b 35%,#e8a0a0 55%,#f0c0b0 70%,#6f7478 100%);" role="img" aria-label="Frozen cocktail being poured at the bar"></div>
  <div class="sticker" style="left:155px;top:63px;width:110px;height:110px;font-size:31px;">OFFER</div>
  <div class="card description">
    <div class="card__date">Description</div>
    <p>Half-price cocktails every Friday from five until seven. Try our house sangria, frozen margaritas and fresh fruit daiquiris, mixed by our friendly bar crew. Happy hour pints and wine by the glass run all week. Ask staff about member discounts tonight.</p>
  </div>
  <div class="social" aria-label="Share"><span></span><span></span><span></span></div>
  <svg class="nav" viewBox="0 0 310 110" aria-label="Navigation">
    <use href="#navBase"/>
    <use href="#iconMeal" x="31" y="70" stroke="var(--icon)" fill="var(--icon)"/>
    <use href="#iconDrink" x="100" y="70" stroke="var(--icon-active)" fill="var(--icon-active)"/>
    <use href="#iconShow" x="179" y="70" stroke="var(--icon)" fill="var(--icon)"/>
    <use href="#iconMembers" x="266" y="70" stroke="var(--icon)"/>
  </svg>
</section>

<!-- Upcoming shows -->
<section class="screen screen--shows">
  <header class="screen__header">Upcoming Shows</header>
  <div class="card" style="left:15px;top:63px;width:173px;height:75px;">
    <div class="card__date">Fri July 20</div>
    <div class="card__act">The Australian RONNIE WALLACE SHOW</div>
  </div>
  <div class="card" style="left:107px;top:152px;width:189px;height:80px;">
    <div class="card__date">Fri Sept 7th</div>
    <div class="card__act card__act--small">Hunger for Thunder<br>The Australian NAILS ‘N’ THORNS SHOW</div>
  </div>
  <div class="card" style="left:8px;top:242px;width:171px;height:75px;">
    <div class="card__date">Fri July 20</div>
    <div class="card__act">The Australian RONNIE WALLACE SHOW</div>
  </div>
  <div class="card" style="left:107px;top:336px;width:189px;height:80px;">
    <div class="card__date">Fri Sept 7th</div>
    <div class="card__act card__act--small">Hunger for Thunder<br>The Australian NAILS ‘N’ THORNS SHOW</div>
  </div>
  <svg class="nav" viewBox="0 0 310 110" aria-label="Navigation">
    <use href="#navBase"/>
    <use href="#iconMeal" x="31" y="70" stroke="var(--icon)" fill="var(--icon)"/>
    <use href="#iconDrink" x="100" y="70" stroke="var(--icon)" fill="var(--icon)"/>
    <use href="#iconShow" x="179" y="70" stroke="var(--icon-active)" fill="var(--icon-active)"/>
    <use href="#iconMembers" x="266" y="70" stroke="var(--icon)"/>
  </svg>
</section>

<!-- Meal deals -->
<section class="screen screen--meals">
  <header class="screen__header">Meal Deals</header>
  <div class="photo" style="left:28px;top:52px;width:248px;height:164px;background:linear-gradient(135deg,#e9d08a 0%,#b46a3a 30%,#6b8e3c 55%,#e8dcc0 80%,#8a6a40 100%);" role="img" aria-label="Quesadilla plate with salsa and salad"></div>
  <div class="sticker" style="left:218px;top:160px;width:56px;height:56px;font-size:24px;">$10</div>
  <div class="photo" style="left:9px;top:224px;width:140px;height:139px;background:linear-gradient(135deg,#f3f3f3 0%,#e1c07a 40%,#cf7a34 55%,#8fae4a 70%,#f0f0f0 100%);" role="img" aria-label="Pasta salad in a white bowl"></div>
  <div class="sticker" style="left:96px;top:304px;width:56px;height:56px;font-size:24px;">$10</div>
  <div class="photo" style="left:163px;top:224px;width:133px;height:126px;background:linear-gradient(135deg,#dfe7c8 0%,#7aa24a 35%,#8a4a2a 60%,#c08050 80%,#eaeaea 100%);" role="img" aria-label="Grilled skewers with green salad"></div>
  <div class="sticker" style="left:240px;top:291px;width:56px;height:56px;font-size:24px;">$10</div>
  <div class="photo" style="left:28px;top:372px;width:248px;height:60px;background:linear-gradient(90deg,#e9d08a 0%,#b46a3a 40%,#6b8e3c 70%,#e8dcc0 100%);" role="img" aria-label="Further meal deal dish"></div>
  <svg class="nav" viewBox="0 0 310 110" aria-label="Navigation">
    <use href="#navBase"/>
    <use href="#iconMeal" x="31" y="70" stroke="var(--icon-active)" fill="var(--icon-active)"/>
    <use href="#iconDrink" x="100" y="70" stroke="var(--icon)" fill="var(--icon)"/>
    <use href="#iconShow" x="179" y="70" stroke="var(--icon)" fill="var(--icon)"/>
    <use href="#iconMembers" x="266" y="70" stroke="var(--icon)"/>
  </svg>
</section>

<p class="caption">Meal deals, drink offers, upcoming shows, members benefits.</p>

</body>
</html>
```